Banner Ad Design Project

We I need three call to action buttons for my new web site. The site is a medical supply company. that should equal 1030x280. The site buttons should say:

1- "EVERYDAY FREE SHIPPING on orders over $50. No code. No hassle."
2- "Call us for FREE EXPERT ADVICE. Click to learn more."
3- "Learn about our QTZ Program. Click to continue"

The site is pelvorantik.com, I need them to replace the flash banner on the home page. I have proper placement, but need them to be distinct colors so they get noticed.

Thank you!

```html
<!DOCTYPE html>
<html lang="en">
<head>
<meta charset="utf-8">
<title>pelvorantik.com – Home Banners</title>
<link href="https://fonts.googleapis.com/css2?family=Marcellus&family=Marcellus+SC&display=swap" rel="stylesheet">
<style>
  :root {
    --canvas-top: #8a8a8a;
    --canvas-bottom: #c9c9c9;
    --banner-white: #ffffff;
    --accent-red: #d6141a;
    --ink-dark: #1d1d1d;
    --ink-soft: #2b2b2b;
    --lilac: #b9a6e6;
    --lilac-soft: #ece6fa;
    --wave-blue: #1b86e6;
    --wave-light: #cfe6fb;
    --rose: #f6c7d8;
    --crimson: #c5122b;
    --button-top: #d9ff6a;
    --button-bottom: #7fcf12;
    --button-edge: #5ea40b;
    --photo-skin: #d9b49c;
    --photo-scrubs: #3d86d2;
    --truck-red: #c51f1f;
  }
  * { box-sizing: border-box; margin: 0; padding: 0; }
  html, body { width: 1200px; height: 1076px; overflow: hidden; }
  body {
    background: linear-gradient(180deg, var(--canvas-top), var(--canvas-bottom));
    font-family: "Marcellus", serif;
    position: relative;
  }
  .banner {
    position: absolute;
    left: 62px;
    width: 1084px;
    height: 294px;
    overflow: hidden;
    background: var(--banner-white);
  }
  .banner--shipping { top: 59px;
    background:
      radial-gradient(ellipse 70% 55% at 40% 105%, var(--lilac) 0%, rgba(185,166,230,0.25) 45%, transparent 70%),
      radial-gradient(ellipse 40% 60% at 95% 10%, var(--lilac-soft) 0%, transparent 70%),
      var(--banner-white);
  }
  .banner--advice { top: 398px;
    background:
      linear-gradient(172deg, var(--banner-white) 42%, var(--wave-light) 55%, var(--wave-blue) 70%, var(--wave-light) 88%, var(--banner-white) 100%);
  }
  .banner--program { top: 723px;
    background: linear-gradient(100deg, #fff6f2 25%, var(--rose) 50%, #e6405a 78%, var(--crimson) 100%);
  }
  .swoosh { position: absolute; inset: 0; width: 100%; height: 100%; }
  .visual { position: absolute; }
  .visual--truck {
    left: 752px; top: 31px; width: 272px; height: 197px;
    background: linear-gradient(160deg, var(--truck-red), #8e1414 70%, #d9c7a8);
    border-radius: 10px;
  }
  .visual--agent {
    left: 0; top: 0; width: 380px; height: 294px;
    background: linear-gradient(120deg, #2a2a2a 0%, var(--photo-skin) 40%, #e7cdbd 75%, rgba(255,255,255,0) 100%);
  }
  .visual--nurse {
    left: 0; top: 0; width: 418px; height: 294px;
    background: linear-gradient(110deg, var(--photo-scrubs) 0%, #5c9be0 45%, #e8eef6 80%, rgba(255,255,255,0) 100%);
  }
  .headline { position: absolute; white-space: nowrap; }
  .shipping__title {
    left: 46px; top: 50px;
    font-size: 43px; color: var(--accent-red); letter-spacing: 0.5px;
  }
  .shipping__note {
    left: 46px; top: 100px;
    font-family: "Marcellus SC", serif;
    font-size: 31px; color: var(--ink-dark);
  }
  .advice__lead {
    right: 30px; top: 56px;
    font-size: 46px; color: var(--accent-red);
  }
  .advice__title {
    right: 30px; top: 112px;
    font-size: 45px; color: var(--accent-red);
  }
  .program__lead, .program__title {
    left: 369px;
    font-family: "Marcellus SC", serif;
    font-size: 42px; color: var(--ink-soft);
    text-shadow: 1px 2px 3px rgba(0,0,0,0.25);
  }
  .program__lead { top: 78px; }
  .program__title { top: 138px; }
  .cta {
    position: absolute;
    left: 724px; top: 217px;
    width: 268px; height: 48px;
    border-radius: 24px;
    background: linear-gradient(180deg, var(--button-top), var(--button-bottom));
    border: 1px solid var(--button-edge);
    box-shadow: 0 3px 6px rgba(0,0,0,0.3), inset 0 2px 2px rgba(255,255,255,0.7);
    display: flex; align-items: center; justify-content: center;
    font-family: "Marcellus SC", serif;
    font-size: 25px; color: var(--ink-dark);
    text-decoration: none;
  }
</style>
</head>
<body>

  <section class="banner banner--shipping">
    <svg class="swoosh" viewBox="0 0 1084 294" aria-hidden="true">
      <path d="M180 294 C 320 200, 520 190, 700 260 L 700 294 Z" fill="#a48fde" opacity="0.35"/>
      <path d="M900 0 C 980 40, 1050 80, 1084 140 L 1084 0 Z" fill="#c9b9f0" opacity="0.5"/>
    </svg>
    <h2 class="headline shipping__title">EVERYDAY FREE SHIPPING</h2>
    <p class="headline shipping__note">on orders over $50. No code. No hassle</p>
    <div class="visual visual--truck" role="img" aria-label="Red delivery truck marked free shipping, loaded with parcels"></div>
  </section>

  <section class="banner banner--advice">
    <div class="visual visual--agent" role="img" aria-label="Photo of a smiling support agent wearing a headset"></div>
    <p class="headline advice__lead">Call us for</p>
    <h2 class="headline advice__title">FREE EXPERT ADVICE</h2>
    <a class="cta" href="#advice">Click to learn more</a>
  </section>

  <section class="banner banner--program">
    <svg class="swoosh" viewBox="0 0 1084 294" aria-hidden="true">
      <path d="M620 294 C 700 150, 850 60, 1084 40" fill="none" stroke="#ffffff" stroke-opacity="0.35" stroke-width="2"/>
      <path d="M660 294 C 740 170, 880 90, 1084 80" fill="none" stroke="#ffffff" stroke-opacity="0.3" stroke-width="2"/>
      <path d="M700 294 C 780 190, 900 120, 1084 120" fill="none" stroke="#ffffff" stroke-opacity="0.25" stroke-width="2"/>
    </svg>
    <div class="visual visual--nurse" role="img" aria-label="Photo of a nurse in blue scrubs with a stethoscope writing on a clipboard"></div>
    <p class="headline program__lead">Learn about</p>
    <h2 class="headline program__title">our QTZ Program</h2>
    <a class="cta" href="#program">Click to Continue</a>
  </section>

</body>
</html>
```